New, modern business card for growing audiology practice

We need a new business card for our audiology practice. Our logo and website have recently changed (more modern) and we want our business cards to reflect this change.
We conduct hearing tests, perform earwax removals, and fit & dispense hearing aids to our patients. We are a family owned practice in which the owner is the one who works directly with the patient. I have attached logos in various formats to use, as well as two ideas I found on this website; as well as a scanned copy of our current logo. Good luck!

Industry/Entity Type

Business

Contact Information for Business Card

Company name: Maplow Hearing Center
Provider name: Peter Mulvoy, Au.D. F/ISN
Phone number: (555) 318-6042
Address: 87 W. Linden Ave. Fernhollow, OH 45990
email: maplowhearing@postvale.net
website: maplowhearing.com

Colors
000000
aaaaaa
dbdbdb
cacaca
9bcb3c
afd23c
cadf82
b1b1b1

Requirements
Must have
• My card must include information in the "details" section. In the attached images, I found a few that I liked and I would like to model after - "brisk tumblin'" and "Sound Wellness Center".
• Must be horizontal.
• Must include logos provided. I uploaded them in various file formats and various ways.
• Must match logo font, if possible, if not, please get as close as you can.
Nice to have
• I really like the idea of having a color on one side with just the logo and company name and the contact information and provider name on the other side. I also really like the idea of having the main color dominating on the logo/company side with accent of that same color on the contact side of the card.
Should not have
• Must not be vertical.

```html
<!DOCTYPE html>
<html lang="en">
<head>
<meta charset="utf-8">
<title>Maplow Hearing Center – Business Card</title>
<link rel="stylesheet" href="https://fonts.googleapis.com/css2?family=Montserrat:wght@300;400;600&display=swap">
<style>
  :root {
    --green: #7aab3e;
    --white: #ffffff;
    --black: #111111;
    --stage: #e6e6e6;
    --card-shadow: rgba(0, 0, 0, 0.18);
  }
  * { margin: 0; padding: 0; box-sizing: border-box; }
  html, body {
    width: 1200px;
    height: 676px;
    overflow: hidden;
    background: var(--stage);
    font-family: "Montserrat", sans-serif;
  }
  .stage {
    width: 1200px;
    height: 676px;
    display: flex;
    align-items: center;
    justify-content: center;
    gap: 60px;
  }
  .card {
    position: relative;
    width: 520px;
    height: 297px;
    box-shadow: 0 10px 26px var(--card-shadow);
    overflow: hidden;
  }

  /* Contact side */
  .card--contact {
    background: var(--green);
    color: var(--white);
    padding: 30px 34px;
  }
  .provider-name {
    font-size: 23px;
    font-weight: 600;
    letter-spacing: 0.2px;
  }
  .provider-title {
    font-size: 14px;
    font-weight: 300;
    margin-top: 2px;
  }
  .address {
    margin-top: 18px;
    font-size: 15px;
    font-weight: 600;
    line-height: 1.35;
  }
  .contact-list {
    list-style: none;
    margin-top: 16px;
    font-size: 15px;
    line-height: 1.4;
  }
  .contact-list .label {
    font-weight: 300;
    margin-right: 4px;
  }
  .contact-list .value { font-weight: 600; }
  .contact-mark {
    position: absolute;
    right: 42px;
    bottom: 46px;
    width: 92px;
    height: 92px;
  }

  /* Brand side */
  .card--brand {
    background: var(--white);
    display: flex;
    flex-direction: column;
  }
  .brand-area {
    flex: 1;
    display: flex;
    align-items: center;
    justify-content: center;
    gap: 12px;
  }
  .brand-dot {
    width: 16px;
    height: 16px;
    border-radius: 50%;
    background: var(--green);
  }
  .brand-name {
    font-size: 24px;
    font-weight: 400;
    letter-spacing: 1px;
    text-transform: uppercase;
    color: var(--black);
  }
  .brand-band {
    height: 62px;
    background: var(--green);
    display: flex;
    align-items: center;
    justify-content: center;
  }
  .brand-web {
    color: var(--white);
    font-size: 14px;
    font-weight: 300;
    letter-spacing: 4px;
  }
</style>
</head>
<body>
<main class="stage">
  <section class="card card--contact" aria-label="Contact side">
    <h1 class="provider-name">Peter Mulvoy, Au.D. F/ISN</h1>
    <p class="provider-title">Owner - Audiologist</p>
    <p class="address">87 W. Linden Ave.<br>Fernhollow, OH 45990</p>
    <ul class="contact-list">
      <li><span class="label">phone</span><span class="value">(555) 318-6042</span></li>
      <li><span class="label">email</span><span class="value">maplowhearing@postvale.net</span></li>
      <li><span class="label">website</span><span class="value">www.maplowhearing.com</span></li>
    </ul>
    <svg class="contact-mark" viewBox="0 0 92 92" aria-hidden="true">
      <circle cx="46" cy="46" r="38" fill="none" stroke="#ffffff" stroke-width="9"/>
    </svg>
  </section>

  <section class="card card--brand" aria-label="Brand side">
    <div class="brand-area">
      <span class="brand-dot"></span>
      <span class="brand-name">Maplow Hearing Center</span>
    </div>
    <div class="brand-band">
      <span class="brand-web">www.maplowhearing.com</span>
    </div>
  </section>
</main>
</body>
</html>
```